Chicken Wing A0 and A4 Poster

Our restaurant name is Tovvra Grill

We have introduced chicken wings to our menu. They are deep fried and mixed with different sauce selections.

The sauce options are: Tovvra BBQ, Regular BBQ, Sweet Chili and Garlic, Hot Chili, Garlic

Available in a 6, 10 or 20 Pack.
Larger Catering Packs Available

We have uploaded some pictures from the internet with chicken wings.

We also have 4 other poster designs coming in the next 3 weeks.

Industry/Entity Type

Restaurant

```html
<!DOCTYPE html>
<html lang="en">
<head>
<meta charset="utf-8">
<title>Tovvra Grill – Chicken Wings Poster</title>
<link href="https://fonts.googleapis.com/css2?family=Arimo:wght@400;700&family=Chewy&display=swap" rel="stylesheet">
<style>
  :root {
    --page-bg: #2b2b2b;
    --magenta: #a3157a;
    --magenta-deep: #4a1050;
    --rose-column: #c9628f;
    --gold: #b8862b;
    --brown: #6b4512;
    --wing-orange: #f6a81c;
    --yellow: #ffe600;
    --cream: #fbf3e2;
    --ink: #111111;
    --white: #ffffff;
  }
  * { margin: 0; padding: 0; box-sizing: border-box; }
  html, body { width: 1200px; height: 2516px; overflow: hidden; }
  body { background: var(--page-bg); font-family: "Arimo", Arial, sans-serif; position: relative; }

  .poster {
    position: absolute; left: 80px; top: 530px;
    width: 1040px; height: 1456px;
    background: var(--magenta); overflow: hidden;
  }
  .top-strip { position: absolute; left: 0; top: 0; width: 1040px; height: 92px; background: var(--cream); }
  .hero-photo {
    position: absolute; left: 282px; top: 92px; width: 758px; height: 560px;
    background: radial-gradient(ellipse at 45% 45%, #c0561a 0%, #8a3410 40%, #e89c52 75%, #f4d2a5 100%);
  }
  .side-photo {
    position: absolute; left: 0; top: 92px; width: 282px; height: 560px;
    background: linear-gradient(180deg, #e8b58a 0%, #c98457 45%, #d9a98d 100%);
    opacity: .85;
  }
  .side-column {
    position: absolute; left: 0; top: 560px; width: 282px; height: 872px;
    background: var(--rose-column);
  }
  .shapes { position: absolute; left: 0; top: 0; }
  .bottom-band { position: absolute; left: 0; bottom: 0; width: 1040px; height: 24px; background: var(--magenta-deep); }

  .brand-ribbon { position: absolute; left: 70px; top: 20px; width: 540px; height: 170px; }
  .brand-name {
    position: absolute; left: 120px; top: 60px; width: 440px; text-align: center;
    font-weight: 700; font-size: 56px; color: var(--white); letter-spacing: 1px;
  }
  .brand-tagline {
    position: absolute; left: 120px; top: 130px; width: 440px; text-align: center;
    font-weight: 700; font-size: 20px; color: var(--white); letter-spacing: 3px;
  }
  .phone-bar {
    position: absolute; left: 650px; top: 68px; width: 390px; height: 74px;
    background: var(--ink); display: flex; align-items: center; gap: 18px; padding-left: 36px;
    color: var(--white); font-weight: 700; font-size: 40px;
  }
  .phone-bar svg { width: 36px; height: 36px; }

  .special-badge { position: absolute; left: 700px; top: 475px; width: 340px; height: 340px; }
  .special-price {
    position: absolute; left: 700px; top: 540px; width: 340px; text-align: center;
    color: var(--yellow); font-weight: 700; font-size: 120px; letter-spacing: -4px; line-height: 1;
  }
  .special-price sup { font-size: 52px; vertical-align: 50px; letter-spacing: 0; }
  .special-label {
    position: absolute; left: 700px; top: 672px; width: 340px; text-align: center;
    color: var(--white); font-weight: 700; font-size: 26px; line-height: 1.1;
  }

  .menu-item { position: absolute; left: 38px; width: 320px; height: 340px; }
  .menu-item.first { top: 690px; }
  .menu-item.second { top: 1064px; }
  .item-photo {
    position: absolute; left: 0; top: 10px; width: 310px; height: 310px; border-radius: 50%;
    border: 10px solid var(--white);
  }
  .first .item-photo { background: radial-gradient(circle at 50% 40%, #9c1b2e 0%, #f2ece6 50%, #c9986a 100%); }
  .second .item-photo { background: radial-gradient(circle at 55% 50%, #7a3a12 0%, #d58b2a 45%, #f3d58f 100%); }
  .item-price {
    position: absolute; left: 236px; top: -30px; width: 120px; height: 120px; border-radius: 50%;
    background: var(--brown); border: 6px solid var(--white);
    color: var(--white); font-weight: 700; font-size: 50px;
    display: flex; align-items: center; justify-content: center;
  }
  .item-name {
    position: absolute; left: 45px; top: 266px; width: 238px; height: 66px; border-radius: 10px;
    background: var(--brown); border: 4px solid var(--white);
    color: var(--white); font-size: 32px; display: flex; align-items: center; justify-content: center;
  }

  .headline { position: absolute; left: 430px; top: 870px; width: 600px; text-align: center; color: var(--white); }
  .headline .lead { font-size: 50px; line-height: 1.2; }
  .headline .dish { font-family: "Chewy", "Comic Sans MS", "Chalkboard SE", sans-serif; color: var(--wing-orange); font-size: 66px; line-height: 1.05; }
  .headline .tail { font-size: 44px; line-height: 1.25; }

  .offer { position: absolute; left: 430px; top: 1082px; width: 600px; text-align: center; color: var(--white); font-size: 25px; line-height: 34px; }
  .offer .sauces b { color: var(--wing-orange); }
  .offer .packs { font-weight: 700; color: var(--yellow); margin-top: 6px; }

  .contact {
    position: absolute; left: 440px; top: 1256px; color: var(--wing-orange);
    font-size: 27px; line-height: 35px; list-style: none;
  }
</style>
</head>
<body>
  <main class="poster">
    <div class="top-strip"></div>
    <div class="side-photo" role="img" aria-label="Faded photo of glazed chicken wings"></div>
    <div class="hero-photo" role="img" aria-label="Photo of saucy deep-fried chicken wings on a plate with herbs"></div>
    <div class="side-column"></div>

    <svg class="shapes" width="1040" height="1456" viewBox="0 0 1040 1456" aria-hidden="true">
      <path d="M282 700 Q620 560 1040 590 L1040 1456 L282 1456 Z" fill="var(--magenta)"/>
      <path d="M170 740 Q600 540 1040 560 L1040 592 Q620 570 282 705 Z" fill="var(--gold)"/>
      <path d="M0 760 Q120 735 170 740 L282 705 L282 760 Z" fill="var(--rose-column)"/>
    </svg>

    <svg class="brand-ribbon" viewBox="0 0 540 170" aria-hidden="true">
      <polygon points="0,20 540,0 520,150 20,170" fill="var(--ink)"/>
      <polygon points="0,20 40,10 20,170" fill="#333"/>
      <polygon points="500,2 540,0 520,150" fill="#333"/>
    </svg>
    <div class="brand-name">Tovvra Grill</div>
    <div class="brand-tagline">AUTHENTIC LEBANESE FOOD</div>

    <div class="phone-bar">
      <svg viewBox="0 0 24 24" aria-hidden="true"><path fill="#ffe600" d="M6.6 10.8a15.1 15.1 0 0 0 6.6 6.6l2.2-2.2a1 1 0 0 1 1-.25 11.4 11.4 0 0 0 3.6.57 1 1 0 0 1 1 1V20a1 1 0 0 1-1 1A17 17 0 0 1 3 4a1 1 0 0 1 1-1h3.5a1 1 0 0 1 1 1c0 1.25.2 2.45.57 3.57a1 1 0 0 1-.25 1z"/></svg>
      <span>555-0142-780</span>
    </div>

    <svg class="special-badge" viewBox="0 0 340 340" aria-hidden="true">
      <g fill="var(--gold)">
        <circle cx="170" cy="170" r="140"/>
        <circle cx="170" cy="40" r="42"/><circle cx="262" cy="78" r="42"/><circle cx="300" cy="170" r="42"/>
        <circle cx="262" cy="262" r="42"/><circle cx="170" cy="300" r="42"/><circle cx="78" cy="262" r="42"/>
        <circle cx="40" cy="170" r="42"/><circle cx="78" cy="78" r="42"/>
      </g>
      <circle cx="170" cy="170" r="140" fill="var(--brown)"/>
    </svg>
    <div class="special-price">$4<sup>.99</sup></div>
    <div class="special-label">TODAY'S<br>SPECIAL</div>

    <section class="menu-item first">
      <div class="item-photo" role="img" aria-label="Photo of chicken wings with a dipping sauce"></div>
      <div class="item-price">$2</div>
      <div class="item-name">6 Pack</div>
    </section>
    <section class="menu-item second">
      <div class="item-photo" role="img" aria-label="Photo of a platter of chicken wings with fries"></div>
      <div class="item-price">$2</div>
      <div class="item-name">20 Pack</div>
    </section>

    <div class="headline">
      <div class="lead">Delicious</div>
      <div class="dish">Chicken Wings</div>
      <div class="tail">that won't hurt your wallet</div>
    </div>

    <div class="offer">
      <p class="sauces"><b>Sauces:</b> Tovvra BBQ · Regular BBQ · Sweet Chili and Garlic · Hot Chili · Garlic</p>
      <p class="packs">6, 10 or 20 Pack · Larger Catering Packs Available</p>
    </div>

    <ul class="contact">
      <li>14 Cedar Lane, Makati City, Metro Manila</li>
      <li>Phone: +63 5550142788</li>
      <li>Email: info@mail.tovvragrill.com</li>
      <li>Facebook: /TovvraGrill</li>
      <li>Twitter: @TovvraGrill</li>
    </ul>

    <div class="bottom-band"></div>
  </main>
</body>
</html>
```